Empower our Electric Journey on the Web

We need a new website that can promote our services. Our three services that we offer are:
- Management of e-mobility charging stations
- Management of energy purchases
- Leasing of E-Mobility charging stations
- Energy billing of private electricity meters
The website should work responsively on PC, tablet and smartphone. In general, a simple navigation and an appealing design should be in the foreground. The website should give the customer the possibility to request , based pm a preset chexkbox chart and to get in contact with us.
Our logo works on black and white background.
Our slogan is:
Empower Your Electric Journey with Velnik Mobility
The 4 Pages should be the following:
Main Page, with info about us, why choose us,
2nd; services; what we sell and what are our services
3rd; Contact us, request an offer
4th, References about costumers and Work we already did, in the future we would like to integrate a Blog Post in this section in stead of references.

Target Market(s)

Landlords, Homeowners, Homeowner Associations

Industry/Entity Type

EV Chargers / E-Mobility

Coding

Coded - Design and coding required

Number of Pages Required

4 page

Requirements
Nice to have
• Pop up to our mailchimp newsletter subscription

```html
<!DOCTYPE html>
<html lang="en">
<head>
<meta charset="utf-8">
<title>Velnik Mobility</title>
<link href="https://fonts.googleapis.com/css2?family=Archivo:wght@800;900&family=Audiowide&family=Exo+2:wght@500;600;800&family=Lexend:wght@300;400;600&display=swap" rel="stylesheet">
<style>
:root{
  --green:#7de449;
  --green-deep:#3db94a;
  --green-pale:#c9efc0;
  --dark:#151515;
  --dark-2:#232323;
  --grey:#d9d9d9;
  --white:#ffffff;
  --ink:#111111;
}
*{margin:0;padding:0;box-sizing:border-box}
html,body{width:1200px;height:4159px;overflow:hidden}
body{position:relative;background:var(--white);font-family:"Lexend",sans-serif;color:var(--ink)}
.abs{position:absolute}
.backdrop{position:absolute;left:0;top:0}
/* header */
.brand{left:84px;top:36px;display:flex;align-items:center;gap:10px;font-family:"Exo 2",sans-serif;font-weight:800;font-size:22px;letter-spacing:2px;color:var(--green)}
.brand-mark{width:14px;height:14px;background:var(--green)}
.nav{top:46px;font-size:12px;color:var(--white);font-family:"Lexend",sans-serif}
.nav-active{border-top:2px solid var(--green-deep);padding-top:6px;top:38px}
.hero-title{left:142px;top:152px;font-family:"Archivo",sans-serif;font-weight:900;font-size:47px;line-height:52px;color:var(--green);text-transform:uppercase}
.btn-outline{border:1.5px solid var(--green);border-radius:14px;font-size:12px;display:flex;align-items:center;justify-content:center}
.dot{width:13px;height:13px;border-radius:50%;background:#777}
.dot.on{background:var(--green-deep)}
.photo{background:linear-gradient(135deg,#555 0%,#2a2a2a 45%,#6b7f8a 100%)}
.intro-title{left:678px;top:455px;font-family:"Archivo",sans-serif;font-weight:900;font-size:46px;line-height:50px;color:var(--green);text-transform:uppercase}
.intro-text{left:678px;top:613px;width:340px;font-size:14.5px;line-height:21px;font-weight:300}
.intro-text b{font-weight:600}
.btn-fill{background:var(--green-deep);color:var(--white);border-radius:14px;font-size:12px;display:flex;align-items:center;justify-content:center}
.section-title{font-family:"Audiowide",sans-serif;color:var(--green-deep)}
/* services */
.service-card{width:391px;height:318px;background:var(--white);overflow:hidden}
.service-card h3{position:absolute;left:0;right:0;top:62px;text-align:center;font-family:"Exo 2",sans-serif;font-weight:500;font-size:33px;line-height:42px;color:var(--ink)}
.service-card .go{position:absolute;left:169px;top:202px}
.service-card .corner{position:absolute;left:0;top:0}
/* about */
.about-text{left:615px;top:2317px;width:505px;font-size:15px;line-height:25px;font-weight:300}
.about-text b{font-weight:600}
.person-name{left:615px;top:2592px;font-family:"Exo 2",sans-serif;font-weight:600;font-size:19px;color:var(--green-deep)}
.person-role{left:615px;top:2617px;font-size:15px;font-weight:300}
.bar{top:2700px;width:37px;height:6px;background:var(--grey)}
.bar.on{background:var(--green)}
/* why */
.why-text{left:84px;top:3362px;width:355px;font-size:15px;line-height:25px;font-weight:300;color:var(--white)}
.feature{left:501px;width:614px;height:141px;background:var(--white)}
.feature .icon-box{position:absolute;left:19px;top:20px;width:102px;height:100px;border:1.5px solid var(--green-deep);display:flex;align-items:center;justify-content:center}
.feature .divider{position:absolute;left:168px;top:20px;width:1px;height:100px;background:#ddd}
.feature h4{position:absolute;left:210px;top:30px;font-size:15px;font-weight:600}
.feature p{position:absolute;left:210px;top:68px;width:380px;font-size:15px;line-height:25px;font-weight:300}
/* cta & footer */
.cta{left:140px;top:3739px;width:918px;height:118px;border-radius:6px;background:linear-gradient(90deg,#7de449 0%,#5dcf44 60%,#43bb3e 100%);box-shadow:0 6px 18px rgba(0,0,0,.35)}
.cta h2{position:absolute;left:67px;top:30px;font-family:"Exo 2",sans-serif;font-weight:800;font-size:48px;color:var(--ink);letter-spacing:.5px}
.cta .talk{position:absolute;left:705px;top:35px;width:142px;height:47px;border:1.5px solid var(--white);border-radius:24px;color:var(--white);font-family:"Exo 2",sans-serif;font-size:25px;display:flex;align-items:center;justify-content:center}
.foot-item{top:3940px;display:flex;gap:8px;font-size:11px;line-height:23px;color:var(--white);font-weight:300}
.social{top:3943px;width:18px;height:14px;border-radius:3px;background:var(--white)}
.legal{top:4115px;font-size:12px;font-weight:300}
</style>
</head>
<body>

<svg class="backdrop" width="1200" height="4159" viewBox="0 0 1200 4159" aria-hidden="true">
  <defs>
    <linearGradient id="heroGrad" x1="0" y1="0" x2="1" y2="1">
      <stop offset="0" stop-color="#1a1a1a"/><stop offset=".55" stop-color="#3a3a3a"/><stop offset="1" stop-color="#111"/>
    </linearGradient>
    <linearGradient id="svcGrad" x1="0" y1="0" x2="1" y2="1">
      <stop offset="0" stop-color="#2b2b2b"/><stop offset=".5" stop-color="#484848"/><stop offset="1" stop-color="#161616"/>
    </linearGradient>
    <linearGradient id="whyGrad" x1="0" y1="0" x2="0" y2="1">
      <stop offset="0" stop-color="#3a3a3a"/><stop offset=".55" stop-color="#1e1e1e"/><stop offset="1" stop-color="#111"/>
    </linearGradient>
  </defs>
  <!-- hero -->
  <polygon points="0,0 1200,0 1200,400 630,400 540,598 0,598" fill="url(#heroGrad)"/>
  <rect x="780" y="0" width="420" height="400" fill="#0d0d0d" role="img" aria-label="Night photo of an electric car headlight"/>
  <polygon points="780,0 1200,0 1200,400 780,400" fill="#1f3520" opacity=".45"/>
  <line x1="1030" y1="0" x2="790" y2="400" stroke="var(--green)" stroke-width="1" opacity=".6"/>
  <line x1="1200" y1="280" x2="1120" y2="400" stroke="var(--green)" stroke-width="1" opacity=".6"/>
  <!-- intro triangle -->
  <polygon points="962,880 890,1009 1051,1009" fill="var(--green)"/>
  <!-- services header line -->
  <polyline points="0,972 678,972 601,1103" fill="none" stroke="#333" stroke-width="1"/>
  <!-- services band -->
  <polygon points="0,1140 700,1140 760,1042 1200,1042 1200,1857 1079,2067 0,2067" fill="url(#svcGrad)" role="img" aria-label="Blurred photo of a road tunnel at night"/>
  <polygon points="698,1224 791,1092 953,1092" fill="var(--green-deep)"/>
  <polygon points="934,1042 1079,1042 1126,1118 980,1118" fill="var(--green)"/>
  <polygon points="1009,1151 1153,1151 1200,1227 1058,1227" fill="var(--green-deep)"/>
  <line x1="1200" y1="1370" x2="1010" y2="1700" stroke="var(--green)" stroke-width="1" opacity=".5"/>
  <!-- about shapes -->
  <polygon points="129,2116 69,2197 202,2220" fill="var(--green)"/>
  <polygon points="0,2288 84,2288 0,2350" fill="var(--green-deep)"/>
  <!-- why section -->
  <polygon points="0,2794 290,2794 350,2890 1200,2890 1200,4086 0,4086" fill="url(#whyGrad)"/>
  <polygon points="630,2980 1200,2980 1200,3115 700,3115" fill="#555" opacity=".35"/>
  <polygon points="0,3115 380,3115 520,3720 0,3720" fill="#444" opacity=".35"/>
  <polygon points="0,3720 1200,3720 1200,4086 0,4086" fill="#141414"/>
</svg>

<!-- header -->
<div class="abs brand"><span class="brand-mark"></span>VELNIK MOBILITY</div>
<div class="abs nav nav-active" style="left:765px">Home</div>
<div class="abs nav" style="left:840px">Services &#8964;</div>
<div class="abs nav" style="left:940px">Past work</div>
<div class="abs nav" style="left:1038px">Contact us &#8964;</div>

<h1 class="abs hero-title">Empower your<br>electric journey<br>with Velnik<br>Mobility</h1>
<div class="abs btn-outline" style="left:142px;top:396px;width:107px;height:27px;color:var(--white)">Learn More</div>
<div class="abs dot on" style="left:143px;top:470px"></div>
<div class="abs dot" style="left:173px;top:470px"></div>
<div class="abs dot" style="left:205px;top:470px"></div>
<div class="abs dot" style="left:236px;top:470px"></div>

<div class="abs" style="left:153px;top:549px;width:397px;height:276px;border:1px solid var(--green-deep)"></div>
<div class="abs photo" style="left:142px;top:536px;width:396px;height:280px;border:1px solid #999" role="img" aria-label="Photo of a charging cable plugged into an electric car"></div>

<h2 class="abs intro-title">Velnik<br>Mobility</h2>
<p class="abs intro-text">Lorem Ipsum is simply dummy text of the printing and typesetting industry. Lorem Ipsum has been the industry's standard dummy text ever since the 1500s, when an unknown printer took a galley of type and scrambled it to make a type <b>specimen book.</b></p>
<div class="abs btn-fill" style="left:678px;top:796px;width:138px;height:28px">Request A Demo</div>
<div class="abs btn-outline" style="left:850px;top:796px;width:108px;height:28px">Learn More</div>

<!-- services -->
<h2 class="abs section-title" style="left:84px;top:1026px;font-size:40px">OUR SERVICES</h2>

<div class="abs service-card" style="left:171px;top:1250px">
  <svg class="corner" width="391" height="318" aria-hidden="true"><polygon points="233,318 330,234 391,234 391,318" fill="var(--green-pale)"/><polygon points="300,318 391,240 391,318" fill="#dff5da"/></svg>
  <h3>Management<br>of E-mobility<br>charging stations</h3>
  <svg class="go" width="54" height="54" viewBox="0 0 54 54" aria-hidden="true"><circle cx="27" cy="27" r="24" fill="none" stroke="var(--green-deep)" stroke-width="4"/><path d="M15 27h22M28 17l10 10-10 10" fill="none" stroke="var(--green-deep)" stroke-width="4" stroke-linecap="round" stroke-linejoin="round"/></svg>
</div>
<div class="abs service-card" style="left:637px;top:1250px">
  <svg class="corner" width="391" height="318" aria-hidden="true"><polygon points="233,318 330,234 391,234 391,318" fill="var(--green-pale)"/><polygon points="300,318 391,240 391,318" fill="#dff5da"/></svg>
  <h3>Management<br>of energy<br>purchases</h3>
  <svg class="go" width="54" height="54" viewBox="0 0 54 54" aria-hidden="true"><circle cx="27" cy="27" r="24" fill="none" stroke="var(--green-deep)" stroke-width="4"/><path d="M15 27h22M28 17l10 10-10 10" fill="none" stroke="var(--green-deep)" stroke-width="4" stroke-linecap="round" stroke-linejoin="round"/></svg>
</div>
<div class="abs service-card" style="left:171px;top:1638px">
  <svg class="corner" width="391" height="318" aria-hidden="true"><polygon points="233,318 330,234 391,234 391,318" fill="var(--green-pale)"/><polygon points="300,318 391,240 391,318" fill="#dff5da"/></svg>
  <h3>Leasing<br>of E-mobility<br>charging stations</h3>
  <svg class="go" width="54" height="54" viewBox="0 0 54 54" aria-hidden="true"><circle cx="27" cy="27" r="24" fill="none" stroke="var(--green-deep)" stroke-width="4"/><path d="M15 27h22M28 17l10 10-10 10" fill="none" stroke="var(--green-deep)" stroke-width="4" stroke-linecap="round" stroke-linejoin="round"/></svg>
</div>
<div class="abs service-card" style="left:637px;top:1638px">
  <svg class="corner" width="391" height="318" aria-hidden="true"><polygon points="233,318 330,234 391,234 391,318" fill="var(--green-pale)"/><polygon points="300,318 391,240 391,318" fill="#dff5da"/></svg>
  <h3>Energy billing<br>of private<br>electricity meters</h3>
  <svg class="go" width="54" height="54" viewBox="0 0 54 54" aria-hidden="true"><circle cx="27" cy="27" r="24" fill="none" stroke="var(--green-deep)" stroke-width="4"/><path d="M15 27h22M28 17l10 10-10 10" fill="none" stroke="var(--green-deep)" stroke-width="4" stroke-linecap="round" stroke-linejoin="round"/></svg>
</div>

<!-- about -->
<div class="abs photo" style="left:84px;top:2220px;width:396px;height:485px;background:linear-gradient(160deg,#e9e9e9 0%,#b8b2a8 55%,#5a5a5a 100%)" role="img" aria-label="Portrait photo of the company owner"></div>
<div class="abs" style="left:103px;top:2242px;width:397px;height:463px;border:1px solid #333"></div>

<h2 class="abs section-title" style="left:615px;top:2214px;font-size:42px">About US</h2>
<p class="abs about-text">Lorem Ipsum is simply dummy text of the printing and typesetting industry. Lorem Ipsum has been the industry's standard dummy text ever since the 1500s, when an unknown took a galley of type and scrambled it to make a type specimen. survived not only five centuries, but also the leap into electronic pesetting, remaining essentially unchanged. It was popularised in the 1960s with the release of Letraset sheets containing Lorem Ipsum passages, and more recently with desktop publishing software like Aldus PageMaker including versions of <b>Lorem Ipsum.</b></p>
<div class="abs person-name">Liam Carter</div>
<div class="abs person-role">Owner/ Creative manager</div>
<div class="abs bar on" style="left:615px"></div>
<div class="abs bar" style="left:672px"></div>
<div class="abs bar" style="left:728px"></div>
<div class="abs bar" style="left:785px"></div>

<!-- why choose us -->
<h2 class="abs section-title" style="left:84px;top:3196px;font-size:40px;color:var(--green)">why choose us</h2>
<div class="abs" style="left:84px;top:3301px;width:37px;height:6px;background:var(--green-deep)"></div>
<p class="abs why-text">Lorem Ipsum is simply dummy text of the printing and typesetting industry. Lorem Ipsum has been the industry's standard dummy text ever since the 1500s, when an unknown took a galley of type and scrambled it to make a type specimen.</p>

<div class="abs feature" style="top:3117px">
  <div class="icon-box"><svg width="60" height="60" viewBox="0 0 60 60" aria-hidden="true"><path d="M12 34v-6a18 18 0 0 1 36 0v6" fill="none" stroke="var(--green-deep)" stroke-width="5"/><rect x="8" y="32" width="10" height="16" rx="4" fill="var(--green-deep)"/><rect x="42" y="32" width="10" height="16" rx="4" fill="var(--green-deep)"/><path d="M47 48c0 5-6 7-14 7" fill="none" stroke="var(--green-deep)" stroke-width="4"/></svg></div>
  <div class="divider"></div>
  <h4>24/7 Support</h4>
  <p>Lorem Ipsum is simply dummy text of the printing and typesetting industry.</p>
</div>
<div class="abs feature" style="top:3282px">
  <div class="icon-box"><svg width="52" height="60" viewBox="0 0 52 60" aria-hidden="true"><path d="M6 4h28l12 12v40H6z" fill="none" stroke="var(--green-deep)" stroke-width="3" stroke-linejoin="round"/><path d="M18 26h10M14 36h24M14 44h24" stroke="var(--green-deep)" stroke-width="3" stroke-linecap="round"/></svg></div>
  <div class="divider"></div>
  <h4>Affordable Cost</h4>
  <p>Lorem Ipsum is simply dummy text of the printing and typesetting industry.</p>
</div>
<div class="abs feature" style="top:3450px">
  <div class="icon-box"><svg width="60" height="40" viewBox="0 0 60 40" aria-hidden="true"><polygon points="2,2 28,20 2,38" fill="var(--green-deep)"/><polygon points="30,2 58,20 30,38" fill="var(--green-deep)"/></svg></div>
  <div class="divider"></div>
  <h4>Fast Delivery</h4>
  <p>Lorem Ipsum is simply dummy text of the printing and typesetting industry.</p>
</div>

<!-- call to action -->
<div class="abs cta">
  <h2>LET’S WORK TOGETHER!</h2>
  <div class="talk">Lets Talk</div>
</div>

<!-- footer -->
<div class="abs foot-item" style="left:140px">
  <svg width="10" height="10" viewBox="0 0 24 24" style="margin-top:7px" aria-hidden="true"><path d="M6 2l4 4-2 3c1 3 4 6 7 7l3-2 4 4-3 4C10 22 2 14 2 5z" fill="var(--white)"/></svg>
  <span>1-800-555-0142</span>
</div>
<div class="abs foot-item" style="left:396px">
  <svg width="11" height="9" viewBox="0 0 24 18" style="margin-top:7px" aria-hidden="true"><rect x="1" y="1" width="22" height="16" fill="none" stroke="var(--white)" stroke-width="2"/><path d="M1 1l11 9 11-9" fill="none" stroke="var(--white)" stroke-width="2"/></svg>
  <span>hello@velnikmobility.com</span>
</div>
<div class="abs foot-item" style="left:648px">
  <svg width="10" height="12" viewBox="0 0 20 24" style="margin-top:6px" aria-hidden="true"><path d="M10 23s8-8 8-13a8 8 0 0 0-16 0c0 5 8 13 8 13z" fill="none" stroke="var(--white)" stroke-width="2"/><circle cx="10" cy="10" r="3" fill="var(--white)"/></svg>
  <span>Velnik Mobility, LLC<br>4210 Harbor Lane Suite 210,<br>Fairview, TX 75069</span>
</div>
<div class="abs social" style="left:962px"></div>
<div class="abs social" style="left:1002px"></div>
<div class="abs social" style="left:1042px"></div>

<div class="abs legal" style="left:84px">© 2023 Welcome. All right reserved.</div>
<div class="abs legal" style="left:861px">Privacy Policy</div>
<div class="abs legal" style="left:1008px">Terms of Service</div>

</body>
</html>
```